TRV Capability Statement Brochure

We need a four or six-page flyer/brochure for our capability statement. This should include all the key written copy and photos/descriptions of the personnel, plus contact addresses in the current capability statement which is attached. We are looking for a modern, professional design that matches our professional approach to our business. Please incorporate our logo into the design.

Target Market(s)

Government departments, shipping companies, port operators, lawyers, export and import businesses, commodity companies.

Industry/Entity Type

Business Consultant

Contact Information for Business Card

Professional, simple to read, uncomplicated.

Font styles to use
Serif
Sans Serif

Colors

Designer to choose colors to be used in the design.

Requirements
Must have
• Company logo
• KEY MESSAGE: Providing independent, expert, confidential and professional services.
• Description of company
• Description and photos of personnel.
• Contact details.
Should not have
• No cliches

```html
<!DOCTYPE html>
<html lang="en">
<head>
<meta charset="utf-8">
<title>TRV Capability Statement – Team Spread</title>
<link href="https://fonts.googleapis.com/css2?family=Arimo:wght@400;700&display=swap" rel="stylesheet">
<style>
:root{
  --bg:#e7ddd7;
  --paper:#fbfbfa;
  --navy:#243450;
  --gold:#d6a52a;
  --ink:#1f1f1f;
}
*{margin:0;padding:0;box-sizing:border-box}
html,body{width:1200px;height:833px;overflow:hidden;background:var(--bg);font-family:"Arimo",Arial,sans-serif;color:var(--ink)}
.spread{position:absolute;left:40px;top:36px;width:1120px;height:760px;display:flex;box-shadow:0 6px 18px rgba(0,0,0,.18)}
.page{position:relative;width:560px;height:760px;background:var(--paper)}
.page--left{border-right:1px solid #ddd}
.hero{position:absolute;left:20px;top:40px;width:520px;height:235px;background:linear-gradient(100deg,#555 0%,#cfcfcf 35%,#f3f3f3 50%,#cfcfcf 65%,#666 100%)}
.section-tag{position:absolute;left:40px;top:300px;width:215px;height:56px;background:var(--navy);color:#fff;font-weight:700;font-size:23px;display:flex;align-items:flex-end;padding:0 0 10px 14px;letter-spacing:.3px}
.services{position:absolute;left:40px;top:368px;width:230px;list-style:none;font-size:9.5px;line-height:1.35}
.services li{margin-bottom:3px;padding-left:8px;position:relative}
.services li::before{content:"•";position:absolute;left:0}
.team-intro{position:absolute;left:290px;top:303px;width:240px}
.team-intro h3{font-size:13px;font-weight:700;margin-bottom:6px}
.team-intro p{font-size:9.3px;line-height:1.3}
.team-heading{position:absolute;left:40px;top:505px;font-size:13px;font-weight:700;letter-spacing:.2px}
.member{position:absolute}
.member .photo{position:absolute;width:105px;height:118px;background:linear-gradient(180deg,#b9b9b9,#5c5c5c)}
.member .bio{position:absolute;font-size:8px;line-height:1.22;padding:0 10px}
.member h4{font-size:12.5px;font-weight:700;display:inline-block;border-bottom:2px solid var(--gold);padding-bottom:1px;margin-bottom:4px;letter-spacing:.3px}
.member p{margin-bottom:3px}
.member .contact{margin-top:2px;margin-bottom:0}
.rule-left{border-left:1px solid var(--gold)}
.rule-right{border-right:1px solid var(--gold)}
.align-right h4{float:right}
.align-right .bio-text{clear:both}
.folio{position:absolute;bottom:22px;display:flex;align-items:center;gap:5px;font-size:9.5px;line-height:1.15;color:var(--ink)}
.folio .num{background:var(--navy);color:#fff;font-weight:700;font-size:15px;width:20px;height:20px;display:flex;align-items:center;justify-content:center}
.folio .label{border-left:1px solid var(--ink);padding-left:4px}
.folio--right{right:30px;text-align:right}
.folio--right .label{border-left:none;border-right:1px solid var(--ink);padding:0 4px 0 0}
.clients{position:absolute;left:30px;top:604px;width:500px;font-size:7.4px;line-height:1.3}
.clients h3{font-size:11.5px;font-weight:700;margin-bottom:3px}
.clients p{margin-bottom:3px}
</style>
</head>
<body>
<div class="spread">
  <section class="page page--left">
    <div class="hero" role="img" aria-label="Black and white photo of two hands joining jigsaw puzzle pieces"></div>
    <div class="section-tag">SUPPLY CHAIN</div>
    <ul class="services">
      <li>Supply chain evaluation and optimisation</li>
      <li>Evaluation and management of tenders and proposal preparation</li>
      <li>Marine project management, project services and support</li>
      <li>Management of bulk and breakbulk logistics</li>
      <li>Stacking analysis for bulk terminals</li>
      <li>Re-engineering of supply chains</li>
    </ul>
    <div class="team-intro">
      <h3>Tiderow Ventures Group Team</h3>
      <p>All team members have decades of commercial shipping industry experience at senior levels and have substantial relevant specialist expertise to offer. With first-class reputations and extensive and diverse backgrounds, the members of the TRV team bring together a capacity quite unique in Australia - for comprehensive evidence-based analysis and evaluation of major maritime and ports projects. We are able to provide innovative solutions to operational problems, a financial evaluation of the alternatives and board-level proposals for change.</p>
    </div>
    <h2 class="team-heading">THE TRV MANAGEMENT TEAM COMPRISES:</h2>
    <article class="member" style="left:40px;top:540px;width:490px;height:150px">
      <div class="photo" style="left:0;top:28px" role="img" aria-label="Portrait photo of Martin Ashdown"></div>
      <div class="bio rule-left" style="left:120px;top:0;width:370px">
        <h4>MARTIN ASHDOWN</h4>
        <p>Martin is a Master Mariner and holds a M.Sc. (Management and Technology; Univ. of Westmere), a B.Sc. (Maritime Studies; Harbourne Polytechnic) and is a Chartered Member of the Chartered Freight Society and an Associate Fellow of the Mariners' Guild. He has over 45 years' experience in the shipping industry.</p>
        <p>A founding member of TRV, Martin was previously General Manager Shipping at Carrick Sugar Limited where he also had roles as Operations Manager and Marine Superintendent between 1983 and 2010. He is a former director of the Coastal Shipowners Council and Mariners Mutual Cover Association Ltd, where he was chairman from 2008-2010. He was also a member of the National Seacover Board from 2006 – 2013.</p>
        <p class="contact">Mob: +61 400 100 201<br>Email: martin@tiderowmarine.com</p>
      </div>
    </article>
    <div class="folio" style="left:30px">
      <span class="num">3</span>
      <span class="label">Tiderow Marine Services<br>Commercial Marine Advisors</span>
    </div>
  </section>

  <section class="page page--right">
    <article class="member" style="left:30px;top:20px;width:500px">
      <div class="photo" style="left:0;top:0" role="img" aria-label="Portrait photo of Graham Pellew"></div>
      <div class="bio rule-left" style="left:115px;top:0;width:385px">
        <h4>GRAHAM PELLEW</h4>
        <p>Graham is a Master Mariner and holds an MBA (Master of Business Administration – Maritime and Logistic Management) and is a Member of the Mariners' Guild. He has over 40 years of experience in the shipping industry.</p>
        <p>A founding member of TRV, Graham was previously Director of Marine Services and Strategic Development with Kestrel Shipping, prior to which he was the General Manager, Business Development for the Kestrel / Orvale joint venture. From 1990 to 2002, Graham held senior positions within Orvale Transport in marine operations, strategic planning and project development and was the Orvale Team Leader on the marine elements of a number of Joint Venture and major infrastructure projects both within Australia and internationally.</p>
        <p class="contact">Mob: +61 400 100 202<br>Email: graham@tiderowmarine.com</p>
      </div>
    </article>

    <article class="member align-right" style="left:30px;top:176px;width:500px">
      <div class="bio rule-right" style="left:0;top:0;width:385px">
        <h4>NEIL CARRAWAY</h4>
        <div class="bio-text">
        <p>Neil has a seafaring background and over 40 years of commercial shipping industry experience. A Fellow of the Guild of Chartered Shipbrokers since 1979, he is a founding partner of TRV. As the Principal of Saltmarsh Chartering since 1985, Neil has extensive knowledge of commercial and operational shipping matters and a wealth of experience in ship sale, purchase and chartering. Saltmarsh provides ship broking and consultancy services to the shipping industry and is part of the Tiderow Ventures Group.</p>
        <p>Neil brings to TRV an extensive network of international contacts in ship sale and purchase, including new buildings; as well as freight markets across all commodity groups.</p>
        <p class="contact">Mob: +61 400 100 203<br>Email: neil@tiderowmarine.com</p>
        </div>
      </div>
      <div class="photo" style="left:395px;top:0" role="img" aria-label="Portrait photo of Neil Carraway"></div>
    </article>

    <article class="member" style="left:30px;top:318px;width:500px">
      <div class="photo" style="left:0;top:0" role="img" aria-label="Portrait photo of Alan Dunmore"></div>
      <div class="bio rule-left" style="left:115px;top:0;width:385px">
        <h4>ALAN DUNMORE</h4>
        <p>Alan has more than 40 years experience in the international maritime and transport industry. A former deep sea mariner, he edited the Australian edition of the shipping industry bible, Harbour Ledger, before becoming a shipping consultant and analyst. Alan has been contracted to provide analysis and advice on major projects with a number of governments, government agencies, ports, shipping and commodity companies, international banks and financial institutions as well as some of the world's leading business consultancies. He has undertaken projects in all Australian states and territories, New Zealand, Asia and islands in the South Pacific.</p>
        <p class="contact">Mob: +61 400 100 204<br>Email: alan@tiderowmarine.com<br>profiles.example/alan-dunmore</p>
      </div>
    </article>

    <article class="member align-right" style="left:30px;top:462px;width:500px">
      <div class="bio rule-right" style="left:0;top:0;width:385px">
        <h4>OWEN HARTLEY</h4>
        <div class="bio-text">
        <p>Owen is an experienced seafarer with a broad range of experience in shipping up to senior management level, along with consulting experience which includes port and tug operations and training. He is also a trained auditor with ongoing experience in ISM, NSCV Safety Management, ISO 9001, 14001 and 18001 management systems. He developed an NSCV safety management system and managed NSCV qualifications for major shipping organisations.</p>
        <p>Owen also conducts training courses for Southern Maritime College. He has a certificate IV in Training and Assessment and is a former General Manager of Halvard Marine Pty Ltd.</p>
        <p class="contact">Mob: +61 400 100 205<br>Email: owen@tiderowmarine.com</p>
        </div>
      </div>
      <div class="photo" style="left:395px;top:0;background:linear-gradient(180deg,#9fb3c4,#e4e8ec)" role="img" aria-label="Portrait photo of Owen Hartley"></div>
    </article>

    <div class="clients">
      <h3>CLIENTS</h3>
      <p>TRV's clientele includes government agencies, all of the major Australian-based resource companies, ports, oil and gas operators, commercial shipping and shipper interests, as well as prominent financial institutions and business consultancies.</p>
      <p>TRV specialises in commercial marine advice and the provision of management support in high-value marine projects. As such, TRV has won the confidence of several Commonwealth Government departments, including Defence (Army and Navy), the Frontier Services Bureau and the National Maritime Safety Office.</p>
    </div>
    <div class="folio folio--right">
      <span class="label">Tiderow Marine Services<br>Commercial Marine Advisors</span>
      <span class="num">4</span>
    </div>
  </section>
</div>
</body>
</html>
```